Flyer/Poster to promote Bicycle Race

We need a flyer that promotes a bicycle race in downtown Denver. It need to inspire spectators to come watch and bicycle racers to come race. It benefits the Tall Pines Cycling Club is getting urban kids on bikes; sharing healthy lifestyle and values
. We want the colors to be the colors of the logo - blue & red. Community Partnerships must have their logos on the flyer. Flyer must be able to be printed in 8 1/2 x 11 and 11 x 17

Target Market(s)

Neighborhood residents, athletes, cyclists

Industry/Entity Type

Non Profit

Font styles to use
Serif
Sans Serif

Colors
0592cd
ec1f27

Requirements
Must have
• Sunday, July 31, 2016
• Schedule:
• • Racing starts at 7:00am
• • Fun Ride on the Race Course at 12pm
• • Expo & Festival 10am – 6pm
• A Bike Race for Amateurs and Professionals
• A Bike Race for the young, the old & everyone in the middle.
• Great for spectators. Hang out, watch the action & explore the Festival
• Grab a bite to eat & cheer on the racers as they fly around the corners
• Special activities for kids: Wobblo Course, Maple the Moose & More!!
• Renaldo Vasquez KPLT Music Director and Crosstown Groove Hour host will be onsite!
• Start/Finish/Festival will be on Larkwell St between 9th Ave & 11th Ave
• Net proceeds benefit the Tall Pines Cycling Club dedicated to getting urban youth on bikes; sharing healthy lifestyle and values
• Special thanks to the Harrowgate Foundation for their ongoing support
• LARKWELLSTCRIT.COM

```html
<!DOCTYPE html>
<html lang="en">
<head>
<meta charset="utf-8">
<title>The Larkwell St Crit – Flyer</title>
<link href="https://fonts.googleapis.com/css2?family=Roboto+Condensed:wght@400;700&family=Lato:wght@400;700&display=swap" rel="stylesheet">
<style>
  :root{
    --race-blue:#0592cd;
    --deep-blue:#0a6fa6;
    --race-red:#ec1f27;
    --dark-red:#c4141b;
    --white:#ffffff;
    --photo-sky:#9fc2cf;
    --photo-road:#8d8f93;
    --ink:#1b1b1b;
  }
  *{margin:0;padding:0;box-sizing:border-box}
  html,body{width:900px;height:1200px;overflow:hidden;background:#ececec}
  .flyer{position:relative;width:900px;height:1200px;overflow:hidden;
    background:linear-gradient(180deg,var(--race-blue) 0%,var(--deep-blue) 100%);
    font-family:"Lato",sans-serif;color:var(--white)}
  .race-photo{position:absolute;left:0;top:0;width:900px;height:640px;
    background:linear-gradient(180deg,#b9d4c8 0%,var(--photo-sky) 22%,#a7a9ad 45%,var(--photo-road) 100%)}
  .event-mark{position:absolute;left:32px;top:0;width:232px;height:210px;
    background:var(--race-blue);display:flex;flex-direction:column;
    align-items:center;justify-content:center;text-align:center;
    clip-path:polygon(0 0,100% 0,100% 88%,50% 100%,0 88%)}
  .event-mark .name{font-family:"Roboto Condensed",sans-serif;font-weight:700;
    font-size:36px;line-height:1.05;color:var(--white);text-transform:uppercase}
  .event-mark .memorial{margin-top:8px;font-family:"Roboto Condensed",sans-serif;
    font-weight:700;font-size:13px;color:var(--white);text-transform:uppercase;letter-spacing:.5px}
  .swoosh{position:absolute;left:0;top:540px;width:900px;height:240px}
  .headline{position:absolute;left:0;width:900px;text-align:center;
    font-family:"Roboto Condensed",sans-serif;font-weight:700;color:var(--white)}
  .headline.lead{top:690px;font-size:44px}
  .headline.main{top:735px;font-size:58px;letter-spacing:.5px}
  .date-pill{position:absolute;left:258px;top:806px;width:582px;height:47px;
    background:var(--race-red);border-radius:6px;display:flex;align-items:center;
    justify-content:center;gap:22px;font-family:"Roboto Condensed",sans-serif;color:var(--white)}
  .date-pill .start{font-size:24px;font-weight:400}
  .date-pill .day{font-size:27px;font-weight:700}
  .details{position:absolute;left:66px;top:868px;width:810px;list-style:none}
  .details li{position:relative;padding-left:26px;font-size:14.6px;line-height:21.6px;color:var(--white)}
  .details li::before{content:"";position:absolute;left:4px;top:6px;width:9px;height:9px;
    border-radius:50%;background:var(--race-red)}
  .partners{position:absolute;left:0;top:1068px;width:900px;display:flex;
    justify-content:center;align-items:center;gap:22px}
  .partner{height:54px;display:flex;align-items:center;justify-content:center;
    background:var(--white);padding:0 8px;font-family:"Lato",sans-serif;font-weight:700;
    font-size:13px;color:var(--ink);text-align:center;line-height:1.1}
  .partner.wide{width:104px}
  .partner.mid{width:92px}
  .partner.dark{background:#111;color:var(--white);width:92px;height:70px}
  .partner.badge{width:66px;height:70px;background:var(--race-red)}
  .light-band{position:absolute;left:0;top:1128px;width:900px;height:8px;background:#d7dde2}
  .footer{position:absolute;left:0;top:1136px;width:900px;height:64px;background:var(--race-red);
    display:flex;align-items:center;justify-content:center}
  .footer .site{font-family:"Lato",sans-serif;font-weight:700;font-size:17px;letter-spacing:1.5px;color:var(--white)}
</style>
</head>
<body>
<main class="flyer">
  <div class="race-photo" role="img" aria-label="Photo of a pack of women cyclists racing down a city street beneath the Dale Harwick Memorial Bicycle Race finish banner"></div>

  <div class="event-mark">
    <span class="name">The Larkwell St Crit</span>
    <span class="memorial">In memory of Dale Harwick</span>
  </div>

  <svg class="swoosh" viewBox="0 0 900 240" preserveAspectRatio="none" aria-hidden="true">
    <path d="M0 70 C220 40 380 110 560 90 C700 75 820 40 900 10 L900 240 L0 240 Z" fill="#dfe6ea"/>
    <path d="M0 92 C230 62 400 128 580 104 C720 86 830 56 900 30 L900 240 L0 240 Z" fill="#3aa9da"/>
    <path d="M0 130 C200 95 420 150 600 110 C730 82 830 55 900 40 L900 240 L0 240 Z" fill="var(--white)"/>
    <path d="M0 142 C210 108 430 162 610 122 C740 93 835 66 900 52 L900 150 C760 150 520 190 300 175 C170 166 60 150 0 160 Z" fill="var(--race-red)"/>
    <path d="M0 160 C60 150 170 166 300 175 C520 190 760 150 900 150 L900 240 L0 240 Z" fill="var(--race-blue)"/>
  </svg>

  <h2 class="headline lead">A Bike Race for</h2>
  <h1 class="headline main">Amateurs and Professionals</h1>

  <div class="date-pill">
    <span class="start">Racing starts at 7:00am</span>
    <span class="day">Sunday, July 31, 2016</span>
  </div>

  <ul class="details">
    <li>A Bike Race for the young, the old &amp; everyone in the middle.</li>
    <li>Great for spectators. Hang out, watch the action &amp; explore the Festival</li>
    <li>Grab a bite to eat &amp; cheer on the racers as they fly around the corners</li>
    <li>Special activities for kids: Wobblo Course, Maple the Moose &amp; More! Renaldo Vasquez KPLT Music Director and</li>
    <li>Crosstown Groove Hour host will be onsite!</li>
    <li>Start/Finish/Festival will be on Larkwell St between 9th Ave &amp; 11th Ave</li>
    <li>Net proceeds benefit the Tall Pines Cycling Club dedicated to getting urban youth on bikes; sharing</li>
    <li>healthy lifestyle and values</li>
    <li>Special thanks to the Harrowgate Foundation for their ongoing support</li>
  </ul>

  <div class="partners">
    <div class="partner wide">Gilded Square</div>
    <div class="partner wide">Velo Nine</div>
    <div class="partner mid">Ardent Realty</div>
    <div class="partner wide">Tall Pines</div>
    <div class="partner mid">Summitwear</div>
    <div class="partner dark">Swift Women's Racing</div>
    <div class="partner badge" aria-label="Partner badge"></div>
  </div>

  <div class="light-band"></div>
  <footer class="footer"><span class="site">www.LARKWELLSTCRIT.COM</span></footer>
</main>
</body>
</html>
```